Wrenhollow Acres Organic Flower Farm, Farmer Florist

I am a flower grower and florist, so I do everything from the field to the vase. I want to include my website, phone, email and instagram

```html
<!DOCTYPE html>
<html lang="en">
<head>
<meta charset="utf-8">
<title>Wrenhollow Acres – Business Card</title>
<link rel="stylesheet" href="https://fonts.googleapis.com/css2?family=Cinzel:wght@400;600&family=Arimo&family=Parisienne&display=swap">
<style>
  :root {
    --backdrop: #1d1d1d;
    --kraft-light: #dfbd93;
    --kraft-mid: #c59b68;
    --kraft-dark: #a87a4a;
    --ink: #141009;
    --rule: #6b4f30;
  }
  * { margin: 0; padding: 0; box-sizing: border-box; }
  html, body { width: 1093px; height: 1200px; overflow: hidden; }
  body { background: var(--backdrop); position: relative; color: var(--ink); }

  .card {
    position: absolute;
    left: 264px;
    width: 580px;
    height: 357px;
    background: linear-gradient(160deg, var(--kraft-light) 0%, var(--kraft-mid) 50%, var(--kraft-dark) 100%);
    text-align: center;
  }
  .card--contact { top: 226px; }
  .card--brand { top: 620px; }

  .abs { position: absolute; left: 0; right: 0; }

  .holder-name {
    top: 68px;
    font-family: "Cinzel", serif;
    font-weight: 600;
    font-size: 25px;
    letter-spacing: 0.5px;
  }
  .holder-role {
    top: 97px;
    font-family: "Arimo", sans-serif;
    font-size: 15.5px;
  }
  .divider {
    display: flex;
    align-items: center;
    justify-content: center;
    gap: 5px;
  }
  .divider__rule { width: 52px; height: 1px; background: var(--rule); }
  .divider--icons { top: 134px; }
  .divider--icons .divider__rule { margin: 0 5px; }
  .icon-box {
    width: 25px; height: 25px;
    background: var(--ink);
    border-radius: 3px;
    display: flex; align-items: center; justify-content: center;
  }
  .icon-box svg { width: 17px; height: 17px; }

  .contact-lines {
    top: 169px;
    font-family: "Arimo", sans-serif;
    font-size: 15.5px;
    line-height: 20.7px;
  }

  .divider--social { top: 245px; }
  .divider--social .divider__rule { width: 68px; margin: 0 6px; }
  .social-dot { width: 27px; height: 27px; border-radius: 50%; background: var(--ink); }
  .social-handle {
    top: 277px;
    font-family: "Arimo", sans-serif;
    font-size: 15.5px;
  }

  .brand-name {
    top: 178px;
    font-family: "Cinzel", serif;
    font-weight: 400;
    font-size: 46px;
    letter-spacing: 4px;
  }
  .brand-tagline {
    top: 236px;
    font-family: "Parisienne", cursive;
    font-size: 27px;
    letter-spacing: 2px;
  }
  .brand-established {
    top: 278px;
    font-family: "Cinzel", serif;
    font-weight: 600;
    font-size: 14px;
    letter-spacing: 5px;
  }
</style>
</head>
<body>
  <section class="card card--contact">
    <h1 class="abs holder-name">NORA PELLHAM</h1>
    <p class="abs holder-role">Farmer Florist</p>

    <div class="abs divider divider--icons">
      <span class="divider__rule"></span>
      <span class="icon-box" aria-label="Phone">
        <svg viewBox="0 0 20 20"><path d="M2 8c0-3 4-4 8-4s8 1 8 4v1h-4V7H6v2H2z M5 10h10l2 6H3z" fill="var(--kraft-light)"/></svg>
      </span>
      <span class="icon-box" aria-label="Email">
        <svg viewBox="0 0 20 20"><rect x="2" y="4" width="16" height="12" fill="none" stroke="var(--kraft-light)" stroke-width="1.5"/><path d="M2 4l8 7 8-7M2 16l6-6M18 16l-6-6" fill="none" stroke="var(--kraft-light)" stroke-width="1.2"/></svg>
      </span>
      <span class="icon-box" aria-label="Website">
        <svg viewBox="0 0 20 20"><circle cx="10" cy="10" r="7.5" fill="none" stroke="var(--kraft-light)" stroke-width="1.5"/><ellipse cx="10" cy="10" rx="3.5" ry="7.5" fill="none" stroke="var(--kraft-light)" stroke-width="1.2"/><path d="M2.5 10h15" stroke="var(--kraft-light)" stroke-width="1.2"/></svg>
      </span>
      <span class="divider__rule"></span>
    </div>

    <address class="abs contact-lines" style="font-style:normal">
      303.555.0148<br>
      nora@wrenhollowacres.com<br>
      www.wrenhollowacres.com
    </address>

    <div class="abs divider divider--social">
      <span class="divider__rule"></span>
      <span class="social-dot"></span>
      <span class="divider__rule"></span>
    </div>
    <p class="abs social-handle">@wrenhollowacres</p>
  </section>

  <section class="card card--brand">
    <h2 class="abs brand-name">WRENHOLLOW</h2>
    <p class="abs brand-tagline">organic flower farm</p>
    <p class="abs brand-established">EST. 2019</p>
  </section>
</body>
</html>
```